Please look at my website to get a better understanding of my business: www.perovatu.com
This business is about Life Coaching for Families, couples, teenagers and individuals. I work more w parents of teenagers (as well as teenagers) but not so much with young kids.
The card should be fun, not too busy, with a sense of flow and playfulness. Warm colors, artistic style (can have a family sculpture, paining or a picture in it). Basic information about myself and my company

Reason: I extended my due date for next Tuesday, November 13th. Please summit new designs if you haven't done so, and for those who submitted, thank you so much for your time and effort. I will make a decision next Tues, and will contact you if I need to revise some items. Much thanks to you all! Orla

Families, parents, teenagers, couples, individuals.

Business

• Business name: PeRoVaTu! Hearth Circle Life Coaching
My name: Orla Bekwith, RMTQ
Description of my work: Tri-Mode life coach
Tel: 555-304-7719
Website: www.PeRoVaTu.com
• Family sculpture, abstract painting or a picture, or simply a nice background w/out a picture added.
• Corporate feeling, cold colors, corporate symbols. no Sunset, or picture of families on the beach.
Don't include bar-code (from uploaded file 1, it is only the designer to find out more about my website).

```html
<!DOCTYPE html>
<html lang="en">
<head>
<meta charset="utf-8">
<title>Orla Bekwith RMTQ – Business Card</title>
<link rel="stylesheet" href="https://fonts.googleapis.com/css2?family=Work+Sans:wght@200;700&display=swap">
<style>
  :root {
    --paper: #ffffff;
    --ink: #111111;
    --band-umber: #7f4520;
    --band-rust: #9c3821;
    --band-orange: #ec6726;
    --band-amber: #f6a91c;
    --band-crimson: #9c1c20;
    --band-h: 46.5px;
  }
  * { margin: 0; padding: 0; box-sizing: border-box; }
  html, body { width: 1200px; height: 804px; overflow: hidden; background: var(--paper); }
  .card {
    position: relative;
    width: 1200px;
    height: 804px;
    background: var(--paper);
    font-family: "Work Sans", "Helvetica Neue", Arial, sans-serif;
    color: var(--ink);
  }
  .family-figures {
    position: absolute;
    left: 52px;
    top: 229px;
    width: 160px;
    height: 128px;
    background: var(--ink);
  }
  .band { position: absolute; left: 0; height: var(--band-h); }
  .band--umber   { top: 365px;   width: 555px;  background: var(--band-umber); }
  .band--rust    { top: 411.5px; width: 555px;  background: var(--band-rust); }
  .band--orange  { top: 458px;   width: 1196px; background: var(--band-orange); }
  .band--amber   { top: 504.5px; width: 555px;  background: var(--band-amber); }
  .band--crimson { top: 551px;   width: 1196px; background: var(--band-crimson); }

  .row {
    position: absolute;
    left: 566px;
    display: flex;
    align-items: baseline;
    white-space: nowrap;
  }
  .row__key {
    width: 72px;
    font-weight: 700;
    font-size: 40px;
    line-height: 1;
  }
  .row__value {
    font-weight: 200;
    font-size: 41px;
    line-height: 1;
    letter-spacing: -0.5px;
  }
  .row--name { top: 367px; }
  .row--title { top: 417px; }
  .row--title .row__value { font-size: 33px; }
  .row--phone { top: 508px; }
  .row--web { top: 554px; color: var(--paper); }
</style>
</head>
<body>
  <main class="card">
    <div class="family-figures" role="img" aria-label="Pictogram of a family: father, mother and baby"></div>

    <div class="band band--umber"></div>
    <div class="band band--rust"></div>
    <div class="band band--orange"></div>
    <div class="band band--amber"></div>
    <div class="band band--crimson"></div>

    <div class="row row--name"><span class="row__key">N</span><span class="row__value">Orla Bekwith RMTQ</span></div>
    <div class="row row--title"><span class="row__key"></span><span class="row__value">Tri-Mode Life Coach</span></div>
    <div class="row row--phone"><span class="row__key">T</span><span class="row__value">555 304 7719</span></div>
    <div class="row row--web"><span class="row__key">W</span><span class="row__value">www.perovatu.com</span></div>
  </main>
</body>
</html>
```